Business Card Design Project

I need a business card design for our new logo, please check the logo at the following link:
https://www.filecrate.net/s/q7rtx2pw9kd41m/FernLoop.png
The address on the business card:
Av. Gervásio Tavares 418 sala 207
Barra da Tijuca, Rio de Janeiro, RJ
CEP: 22714-380
Brasil
Phone: +55 21 86347215
e-mail: osvaldo@fernloop.com.br
Updates
Thank you all for sending your designs, we will not provide feedback because there are too many designs, on December 3 we will pick the best design according to our point of view. Please keep posting.
Osvaldo
Industry/Entity Type
Business
Look and feel
Each slider illustrates characteristics of the customer's brand and the style your logo design should communicate.

```html
<!DOCTYPE html>
<html lang="pt-BR">
<head>
<meta charset="utf-8">
<title>FernLoop — Business Card</title>
<link href="https://fonts.googleapis.com/css2?family=Source+Sans+3:wght@400;600;700&display=swap" rel="stylesheet">
<style>
  :root {
    --stage: #e9e6e1;
    --card-black: #141414;
    --card-black-soft: #2a2d2b;
    --band-yellow: #f2b705;
    --band-yellow-deep: #d99a00;
    --card-silver: #f4f4f4;
    --card-silver-shade: #c9c9c9;
    --band-dark: #1b1b1b;
    --ink: #1e1e1e;
    --ink-soft: #3a3a3a;
    --paper-white: #ffffff;
  }
  * { margin: 0; padding: 0; box-sizing: border-box; }
  html, body {
    width: 1200px; height: 900px; overflow: hidden;
    background: var(--stage);
    font-family: "Source Sans 3", "Myriad Pro", Arial, sans-serif;
  }
  .stage {
    width: 1200px; height: 900px;
    display: flex; flex-direction: column; align-items: center; justify-content: center;
    gap: 60px;
  }
  .card {
    position: relative;
    width: 620px; height: 354px;
    overflow: hidden;
    box-shadow: 0 10px 28px rgba(0,0,0,0.25);
  }
  .card-front {
    background: radial-gradient(ellipse at 55% 40%, var(--card-black-soft), var(--card-black) 70%);
  }
  .card-front .band {
    position: absolute; left: 0; right: 0; height: 20px;
    background: linear-gradient(to bottom, var(--band-yellow), var(--band-yellow-deep));
  }
  .card-front .band-top { top: 0; }
  .card-front .band-bottom { bottom: 0; height: 24px; }
  .front-logo {
    position: absolute; left: 0; right: 0; top: 120px;
    display: flex; align-items: center; justify-content: center; gap: 14px;
  }
  .front-logo .mark {
    width: 30px; height: 30px; border-radius: 50%;
    background: var(--paper-white);
  }
  .front-logo .wordmark {
    font-size: 52px; font-weight: 700; color: var(--paper-white); letter-spacing: 0.5px;
  }
  .front-url {
    position: absolute; left: 0; right: 0; bottom: 52px;
    text-align: center;
    font-size: 22px; font-weight: 600; color: var(--paper-white); letter-spacing: 0.5px;
  }
  .card-back {
    background: linear-gradient(115deg, var(--card-silver-shade) 0%, var(--card-silver) 35%, var(--paper-white) 55%, var(--card-silver-shade) 100%);
  }
  .card-back .band {
    position: absolute; left: 0; right: 0; height: 16px; background: var(--band-dark);
  }
  .card-back .band-top { top: 0; }
  .card-back .band-bottom { bottom: 0; height: 18px; }
  .back-logo {
    position: absolute; left: 30px; top: 62px;
    display: flex; align-items: center; gap: 10px;
  }
  .back-logo .mark {
    width: 22px; height: 22px; border-radius: 50%; background: var(--band-yellow);
  }
  .back-logo .wordmark {
    font-size: 38px; font-weight: 700; color: var(--ink);
  }
  .contact {
    position: absolute; right: 32px; top: 110px;
    text-align: right; color: var(--ink);
  }
  .contact .name { font-size: 21px; font-weight: 700; }
  .contact .role { font-size: 14px; color: var(--ink-soft); margin-top: 1px; }
  .contact .address {
    font-style: normal; font-size: 16px; line-height: 1.4; margin-top: 22px;
  }
  .contact-line {
    position: absolute; right: 32px; bottom: 46px;
    font-size: 16px; color: var(--ink);
  }
  .contact-line b { font-weight: 700; }
</style>
</head>
<body>
<main class="stage">
  <section class="card card-front" aria-label="Business card front">
    <div class="band band-top"></div>
    <div class="front-logo">
      <span class="mark"></span>
      <span class="wordmark">FernLoop</span>
    </div>
    <p class="front-url">www.fernloop.com.br</p>
    <div class="band band-bottom"></div>
  </section>

  <section class="card card-back" aria-label="Business card back">
    <div class="band band-top"></div>
    <div class="back-logo">
      <span class="mark"></span>
      <span class="wordmark">FernLoop</span>
    </div>
    <div class="contact">
      <p class="name">Osvaldo Ferraz</p>
      <p class="role">President</p>
      <address class="address">
        Av. Gervásio Tavares 418 sala 207<br>
        Barra da Tijuca, Rio de Janeiro, RJ<br>
        CEP: 22714-380, Brasil
      </address>
    </div>
    <p class="contact-line"><b>P:</b> +55 21 86347215 | <b>E:</b> osvaldo@fernloop.com.br</p>
    <div class="band band-bottom"></div>
  </section>
</main>
</body>
</html>
```